Brantley Advisory Group provides support for renewable energy projects to utilities and suppliers

I need a professional looking business card that is both simple and elegant and unique. My clients are mostly large organizations not individuals. I am a consultant with my own company that is small but would like to give clients the impression I am larger. Smart grid, fiber optics, software, field hardware, distribution automation, substation automation, operations, energy storage/batteries, microgrids, customer service, strategy/roadmaps, conservation, Automated Metering Infrastruture (AMI or smart meters) are all areas of focus.

Target Market(s)

Utilities, suppliers, governmental agencies involved in energy. All types of energy especially natural gas and electrical. Especially renewable energy or green projects.

Contact Information for Business Card

Name - Mark Brantley Cell Phone - 425.318.2746 Email - mbrantley@brantleyag-example.com
Company - Brantley Advisory Group (logo) Title - Principal

Font styles to use
Serif
Sans Serif

Colors

Designer to choose colors to be used in the design.

Requirements
Must have
• Simple and professional and powerful.
• Unique/creative design.
Nice to have
• Utilize color scheme to accent logo colors. Maybe some geometric pattern on edge of card with color.
Should not have
• Busy, complicated, traditional

```html
<!DOCTYPE html>
<html lang="en">
<head>
<meta charset="utf-8">
<title>Brantley Advisory Group – Business Card</title>
<link rel="stylesheet" href="https://fonts.googleapis.com/css2?family=Roboto:wght@400;700&display=swap">
<style>
  :root {
    --backdrop: #c4c5c7;
    --brand-blue: #1c3f94;
    --brand-blue-light: #2a4da3;
    --brand-green: #66913d;
    --ink: #1d1d1f;
    --rule: #a9aaac;
    --paper: #ffffff;
  }
  * { box-sizing: border-box; margin: 0; padding: 0; }
  html, body {
    width: 1200px; height: 1124px; overflow: hidden;
    background: var(--backdrop);
    font-family: "Roboto", Arial, sans-serif;
  }
  .canvas { position: relative; width: 1200px; height: 1124px; }

  /* Front side */
  .card-front {
    position: absolute; left: 335px; top: 103px;
    width: 748px; height: 428px;
    background: var(--paper);
    border: 1px solid var(--rule);
    border-radius: 100px 0 100px 0;
    overflow: hidden;
  }
  .card-front .accents { position: absolute; inset: 0; }
  .brand-lockup {
    position: absolute; left: 92px; top: 168px;
    display: flex; align-items: center; gap: 16px;
  }
  .brand-mark {
    width: 44px; height: 44px;
    border: 3px solid var(--brand-green);
    border-radius: 4px;
    flex: none;
  }
  .brand-name {
    color: var(--brand-blue);
    font-weight: 700;
    font-size: 25px;
    line-height: 1.15;
  }
  .divider {
    position: absolute; left: 402px; top: 120px;
    width: 2px; height: 183px;
    background: var(--rule);
  }
  .contact {
    position: absolute; left: 426px; top: 118px;
    color: var(--ink);
  }
  .contact-name { color: var(--brand-blue); font-weight: 700; font-size: 23px; line-height: 28px; }
  .contact-title { color: var(--brand-green); font-size: 20px; line-height: 26px; }
  .contact-address { margin-top: 10px; font-size: 19px; line-height: 25px; }
  .contact-line {
    display: flex; align-items: center; gap: 12px;
    font-size: 19px; line-height: 24px;
  }
  .contact-line.phone { margin-top: 16px; }
  .contact-line.email { margin-top: 10px; font-size: 16px; }
  .contact-line svg { width: 19px; height: 16px; flex: none; }

  /* Back side */
  .card-back {
    position: absolute; left: 86px; top: 589px;
    width: 748px; height: 426px;
    border-radius: 100px 0 100px 0;
    overflow: hidden;
  }
  .card-back .texture {
    position: absolute; inset: 0;
    background: linear-gradient(135deg, var(--brand-blue-light) 0%, var(--brand-blue) 60%, #1a3a8a 100%);
  }
  .back-lockup {
    position: absolute; left: 160px; top: 150px;
    display: flex; align-items: center; gap: 26px;
  }
  .back-lockup .brand-mark {
    width: 84px; height: 84px;
    border: 5px solid var(--paper);
    border-radius: 6px;
  }
  .back-lockup .brand-name {
    color: var(--paper);
    font-size: 46px;
    line-height: 1.1;
  }
</style>
</head>
<body>
<main class="canvas">

  <section class="card-front" aria-label="Business card front">
    <svg class="accents" viewBox="0 0 748 428" width="748" height="428" aria-hidden="true">
      <path d="M0,0 L139,0 C70,22 22,90 0,168 Z" fill="var(--brand-blue)"/>
      <path d="M748,296 C730,360 690,410 637,428 L748,428 Z" fill="var(--brand-green)"/>
    </svg>

    <div class="brand-lockup">
      <span class="brand-mark"></span>
      <div class="brand-name">Brantley<br>Advisory Group</div>
    </div>

    <div class="divider"></div>

    <div class="contact">
      <p class="contact-name">Mark Brantley</p>
      <p class="contact-title">Principal</p>
      <p class="contact-address">Street Name, City Name<br>Zipcode - 012345</p>
      <p class="contact-line phone">
        <svg viewBox="0 0 19 16" aria-hidden="true">
          <path d="M3,1 L6,1 L7.5,4.5 L5.5,6 C6.8,8.6 8.8,10.6 11.5,12 L13,10 L16.5,11.5 L16.5,14.5 C16.5,15 16,15.5 15.5,15.5 C8.5,15 2.5,9 2,2 C2,1.5 2.5,1 3,1 Z" fill="var(--brand-green)"/>
        </svg>
        425.318.2746
      </p>
      <p class="contact-line email">
        <svg viewBox="0 0 19 16" aria-hidden="true">
          <rect x="0.5" y="2.5" width="18" height="12" fill="var(--brand-green)"/>
          <path d="M1,3 L9.5,9.5 L18,3 M1,14 L7,8 M18,14 L12,8" stroke="#fff" stroke-width="1.4" fill="none"/>
        </svg>
        mbrantley@brantleyag-example.com
      </p>
    </div>
  </section>

  <section class="card-back" aria-label="Business card back">
    <div class="texture" role="img" aria-label="Deep blue background with a faint repeating pattern of overlapping outlined squares"></div>
    <div class="back-lockup">
      <span class="brand-mark"></span>
      <div class="brand-name">Brantley<br>Advisory Group</div>
    </div>
  </section>

</main>
</body>
</html>
```